Income Tax and Accounting Brochure

I need a brochure using my new logo (file attached). I do tax work and accounting work. I am an EA (QDX Enrolled Agent - logo attached) and would like this incorporated into the brochure. I also have a MSA in Accounting. Please incorporate the text that I have provided in the brochure.

Target Market(s)

Tax Clients - both business and individuals

Industry/Entity Type

Accounting

Colors
0054AA
0677BA
7BADD7
CADEEF
E8F1F8

Requirements
Must have
• Use my logo and the QDX EA file in the brochure
Nice to have
• I would like to see a brochure that I can customize with my own text if possible.

```html
<!DOCTYPE html>
<html lang="en">
<head>
<meta charset="utf-8">
<title>HDL Accounting &amp; Consulting – Brochure</title>
<link rel="stylesheet" href="https://fonts.googleapis.com/css2?family=Poppins:wght@400;700&family=Oswald:wght@400;700&display=swap">
<style>
  :root {
    --page: #ffffff;
    --orange: #f0801f;
    --white: #ffffff;
    --navy-deep: #1d3a58;
    --steel: #3f6a8e;
    --steel-light: #5f8fb4;
    --band: rgba(6, 84, 170, 0.55);
    --fold: rgba(255, 255, 255, 0.18);
  }
  * { margin: 0; padding: 0; box-sizing: border-box; }
  html, body { width: 855px; height: 1200px; overflow: hidden; background: var(--page); }
  body { position: relative; font-family: "Poppins", sans-serif; color: var(--white); }

  .spread { position: absolute; left: 32px; width: 790px; height: 559px; overflow: hidden; }
  .spread--outside { top: 25px; }
  .spread--inside { top: 614px; }

  .spread__photo { position: absolute; inset: 0; }
  .spread--outside .spread__photo {
    background:
      radial-gradient(ellipse at 78% 55%, rgba(150,185,215,0.55), transparent 55%),
      radial-gradient(ellipse at 55% 25%, rgba(120,165,205,0.5), transparent 60%),
      linear-gradient(180deg, #4d7aa0 0%, #416c92 45%, #2c4d6c 80%, #1f3a55 100%);
  }
  .spread--inside .spread__photo {
    background:
      radial-gradient(ellipse at 80% 85%, rgba(160,185,210,0.55), transparent 50%),
      radial-gradient(ellipse at 45% 90%, rgba(140,165,195,0.45), transparent 45%),
      linear-gradient(180deg, #46729a 0%, #4a7399 45%, #5f82a4 70%, #6c89a6 100%);
  }

  .fold { position: absolute; top: 0; bottom: 0; width: 1px; background: var(--fold); }
  .fold--one { left: 263px; }
  .fold--two { left: 526px; }

  .panel { position: absolute; top: 0; height: 100%; width: 263px; }
  .panel--left { left: 0; }
  .panel--middle { left: 263px; }
  .panel--right { left: 526px; }

  .panel__heading {
    position: absolute; left: 26px; top: 24px; width: 220px;
    font-weight: 700; font-size: 12.6px; line-height: 14.5px; color: var(--orange);
  }
  .panel__body {
    position: absolute; left: 26px; width: 222px;
    font-size: 11.4px; line-height: 13.5px;
  }
  .panel__body p + p { margin-top: 13.5px; }

  .about .panel__body { top: 67px; }

  .contact .panel__heading { top: 24px; }
  .contact__list { position: absolute; left: 26px; top: 43px; list-style: none; font-size: 11.4px; line-height: 19.1px; }

  .brand { position: absolute; left: 54px; top: 38px; display: flex; align-items: center; gap: 8px; }
  .brand__mark { width: 32px; height: 32px; border-radius: 50%; background: var(--white); flex: none; }
  .brand__name { font-weight: 400; font-size: 10.5px; line-height: 12.5px; letter-spacing: 0.6px; color: var(--white); }

  .headline-band {
    position: absolute; left: 0; top: 94px; width: 263px; height: 71px;
    background: var(--band); text-align: center;
    font-family: "Oswald", sans-serif; color: var(--orange);
  }
  .headline-band__lead { display: block; margin-top: 10px; font-size: 18.5px; font-weight: 400; line-height: 22px; letter-spacing: -0.2px; }
  .headline-band__main { display: block; font-size: 26px; font-weight: 700; line-height: 30px; letter-spacing: 0.4px; }

  .inside-heading { top: 24px; }
  .tax .panel__body { top: 48px; }

  .benefits .panel__heading { left: 37px; }
  .benefits__list { position: absolute; left: 12px; top: 47px; width: 244px; list-style: none; font-size: 11.4px; line-height: 13.5px; }
  .benefits__item { position: relative; padding-left: 25px; }
  .benefits__item + .benefits__item { margin-top: 13.5px; }
  .benefits__tick { position: absolute; left: 0; top: -1px; width: 17px; height: 17px; }

  .books .panel__body { top: 47px; line-height: 17.2px; width: 226px; }
</style>
</head>
<body>

<section class="spread spread--outside">
  <div class="spread__photo" role="img" aria-label="Businessman in a suit pointing at rising arrow graphics on a blue background"></div>
  <div class="fold fold--one"></div>
  <div class="fold fold--two"></div>

  <article class="panel panel--left about">
    <h2 class="panel__heading">About Harriet D Lowell, MSA EA (Principal)</h2>
    <div class="panel__body">
      <p>I have a Masters' Degree in accounting and am an QDX Enrolled Agent.</p>
      <p>I am also a LedgerBooks Advanced Certified Consultant in both the online and desktop products including Enterprise and Point of Sale.</p>
      <p>I provide individual and small business tax services, Accounting, bookkeeping, QDX representation, insurance audit representation, business license assistance and more.</p>
      <p>I have experience working with a wide variety of clients from the point where they first decide they want to start a business. They are often unsure about what to do first- I have a lot of experience to offer you.</p>
    </div>
  </article>

  <article class="panel panel--middle contact">
    <h2 class="panel__heading">Contact Us</h2>
    <ul class="contact__list">
      <li>Address:</li>
      <li>HDL Accounting &amp; Consulting, LLC</li>
      <li>4820 Maple Hollow Rd, PO Box 17</li>
      <li>Brookfield, VA 20990</li>
      <li>Phone:</li>
      <li>(555)214-0387</li>
      <li>Fax:</li>
      <li>(555)613-2294</li>
      <li>Email:</li>
      <li>hdlaccounting@mailbox.example</li>
      <li>Website:</li>
      <li>www.hdlaccounting.example</li>
    </ul>
  </article>

  <article class="panel panel--right cover">
    <div class="brand">
      <span class="brand__mark"></span>
      <span class="brand__name">HDL ACCOUNTING &amp;<br>CONSULTING, LLC</span>
    </div>
    <h1 class="headline-band">
      <span class="headline-band__lead">WHAT A JOY IT IS TO WATCH</span>
      <span class="headline-band__main">SUCCESS IN ACTION!</span>
    </h1>
  </article>
</section>

<section class="spread spread--inside">
  <div class="spread__photo" role="img" aria-label="Handshake over a desk with coffee, and colleagues reviewing paperwork with a calculator"></div>
  <div class="fold fold--one"></div>
  <div class="fold fold--two"></div>

  <article class="panel panel--left tax">
    <h2 class="panel__heading inside-heading">Tax Preparation – why hire us?</h2>
    <div class="panel__body">
      <p>Preparing your own income tax return can be a task that leaves you with more questions than answers.</p>
      <p>According to a study released by the US Government's National Revenue Review Office last year, most taxpayers (%77 of 71 million taxpayers) believe they benefited from using a professional tax preparer.</p>
      <p>Whether we like it or not, today's tax laws are so complicated that filing a relatively simple return can be confusing.</p>
      <p>It is just too easy to overlook deductions and credits to which you are entitled.</p>
      <p>Even if you use a computer software program there's no substitute for the assistance of an experienced tax professional.</p>
    </div>
  </article>

  <article class="panel panel--middle benefits">
    <h2 class="panel__heading inside-heading">Here's what your get...</h2>
    <ul class="benefits__list">
      <li class="benefits__item">
        <svg class="benefits__tick" viewBox="0 0 20 20" aria-hidden="true"><path d="M17.2 6.2A8.5 8.5 0 1 0 18.5 10" fill="none" stroke="#f0801f" stroke-width="1.6" stroke-linecap="round"/><path d="M6 9.6l3.2 3.2 8.4-8.6" fill="none" stroke="#f0801f" stroke-width="1.8" stroke-linecap="round" stroke-linejoin="round"/></svg>
        Your tax return will be checked and rechecked by our computer software identifying potential problems the QDX may look at more closely and reviewing the math to limit QDX contacts.
      </li>
      <li class="benefits__item">
        <svg class="benefits__tick" viewBox="0 0 20 20" aria-hidden="true"><path d="M17.2 6.2A8.5 8.5 0 1 0 18.5 10" fill="none" stroke="#f0801f" stroke-width="1.6" stroke-linecap="round"/><path d="M6 9.6l3.2 3.2 8.4-8.6" fill="none" stroke="#f0801f" stroke-width="1.8" stroke-linecap="round" stroke-linejoin="round"/></svg>
        Your tax return can be filed electronically so you will get a refund back quicker.
      </li>
      <li class="benefits__item">
        <svg class="benefits__tick" viewBox="0 0 20 20" aria-hidden="true"><path d="M17.2 6.2A8.5 8.5 0 1 0 18.5 10" fill="none" stroke="#f0801f" stroke-width="1.6" stroke-linecap="round"/><path d="M6 9.6l3.2 3.2 8.4-8.6" fill="none" stroke="#f0801f" stroke-width="1.8" stroke-linecap="round" stroke-linejoin="round"/></svg>
        Our staff will show you how to adjust your payroll withholding to get more money back each week. Why give the QDX an interest free loan for up to 16 months.
      </li>
      <li class="benefits__item">
        <svg class="benefits__tick" viewBox="0 0 20 20" aria-hidden="true"><path d="M17.2 6.2A8.5 8.5 0 1 0 18.5 10" fill="none" stroke="#f0801f" stroke-width="1.6" stroke-linecap="round"/><path d="M6 9.6l3.2 3.2 8.4-8.6" fill="none" stroke="#f0801f" stroke-width="1.8" stroke-linecap="round" stroke-linejoin="round"/></svg>
        We will show you potential deductions to limit your tax liability for next year. In addition, we will give you a sheet of commonly overlooked deductions to limit the following year's tax liability.
      </li>
    </ul>
  </article>

  <article class="panel panel--right books">
    <h2 class="panel__heading inside-heading">Books a Mess: No Problem!</h2>
    <div class="panel__body">
      If you own a small business and haven't kept up your bookkeeping, don't worry. We can help you.<br>
      We'll prepare your bookkeeping for the year, prepare a full Schedule C, as well as your personal income tax return.<br>
      Then we'll help you set up an easy system that allows you to keep your books in tip-top shape next year.
    </div>
  </article>
</section>

</body>
</html>
```